Digital Asset Exchange (Trading Platform)

We need a design of Digital Asset Exchange Trading Platform.

Please find attached a mock up of LumaVoltix design this has to be redesigned based on fenrow.example style.

Industry/Entity Type

Digital

```html
<!DOCTYPE html>
<html lang="en">
<head>
<meta charset="utf-8">
<title>LumaVoltix Exchange</title>
<link href="https://fonts.googleapis.com/css2?family=Open+Sans:wght@400;600;700;800&family=Droid+Serif&family=Noto+Serif:wght@400&display=swap" rel="stylesheet">
<style>
:root{
  --orange:#f28c1e;
  --orange-dark:#d9700a;
  --red:#d8281c;
  --ink:#2a2a2a;
  --text:#666;
  --muted:#999;
  --page:#ffffff;
  --hero:#efefef;
  --panel:#f4f4f4;
  --line:#dcdcdc;
  --dark:#1c1c1c;
  --dark-2:#2b2b2b;
}
*{box-sizing:border-box;margin:0;padding:0}
html,body{width:796px;height:1200px;overflow:hidden}
body{position:relative;background:var(--page);font-family:"Open Sans",Arial,sans-serif;color:var(--text);font-size:10px}
.abs{position:absolute}

/* header */
.site-header{left:0;top:0;width:796px;height:70px;background:linear-gradient(#2c2c2c,#141414)}
.brand{left:40px;top:20px;display:flex;align-items:center;gap:9px;color:#fff;font-weight:700;font-size:21px}
.brand-dot{width:28px;height:28px;border-radius:50%;background:var(--orange)}
.main-nav{right:60px;top:0;display:flex;height:70px}
.main-nav a{display:flex;align-items:center;padding:0 17px;color:#ddd;text-decoration:none;font-size:11px;font-weight:600;letter-spacing:.5px}
.main-nav a.active{color:var(--orange);border-bottom:3px solid var(--orange)}

/* hero */
.hero{left:0;top:70px;width:796px;height:280px;background:linear-gradient(#f7f7f7,#e7e7e7)}
.hero-title{left:74px;top:42px;color:var(--orange);font-size:25px;font-weight:800}
.hero-text{left:74px;top:82px;width:260px;font-size:10.5px;line-height:15px;font-weight:600;color:#555;text-transform:uppercase}
.hero-actions{left:74px;top:170px;display:flex;gap:8px}
.btn{background:var(--orange);color:#fff;font-size:9px;font-weight:700;padding:6px 10px;border-radius:2px}
.hero-art{left:340px;top:10px;width:370px;height:262px;background:linear-gradient(180deg,#f3efe6 0%,#e4dccd 55%,#f2c27c 75%,#d8d2c6 100%);border-radius:4px}

/* features */
.feature{top:372px;width:204px;height:146px;background:#fff;border:1px solid var(--line);border-radius:4px;box-shadow:0 3px 6px rgba(0,0,0,.12)}
.feature h3{font-size:15px;font-weight:600;color:var(--ink);padding:14px 14px 8px;border-bottom:1px solid var(--line)}
.feature p{font-size:9.5px;line-height:13px;padding:9px 14px;color:var(--text)}
.feature .more{position:absolute;left:0;right:0;bottom:8px;text-align:center;font-size:8px;font-weight:700;color:var(--ink)}
.feature .more i{display:block;width:14px;height:14px;margin:3px auto 0;border-radius:50%;background:var(--orange)}
.feature.highlight{background:var(--orange);border-color:var(--orange-dark)}
.feature.highlight h3{color:#fff;border-color:rgba(255,255,255,.4)}
.feature.highlight p{color:#fff}
.feature-icon{position:absolute;right:14px;top:12px;width:22px;height:22px}

/* market */
.section-title{font-size:22px;font-weight:700;color:var(--ink)}
.market-title{left:74px;top:556px}
.market-rule{left:74px;top:590px;width:400px;height:1px;background:var(--line)}
.market-stats{left:74px;top:602px;width:400px;display:flex;justify-content:space-between;font-size:11px;color:#555}
.chart{left:74px;top:624px;width:400px;height:250px;background:var(--panel);border:1px solid var(--line)}
.chart-tabs{position:absolute;left:12px;top:10px;display:flex;gap:3px}
.chart-tabs span{font-size:8px;padding:3px 6px;background:#e2e2e2;color:#777}
.chart-tabs span.on{background:var(--orange);color:#fff}

.news-tabs{left:505px;top:562px;display:flex}
.news-tabs span{color:#fff;font-weight:700;font-size:14px;padding:4px 14px}
.tab-news{background:var(--orange)}
.tab-old{background:var(--red);padding:4px 26px!important}
.news-list{left:505px;top:600px;width:216px}
.news-item{display:flex;gap:9px;height:68px;border-bottom:1px dotted var(--line);padding-top:6px}
.date{width:34px;height:38px;background:var(--orange);color:#fff;text-align:center;flex:none}
.date b{display:block;font-size:15px;line-height:22px}
.date small{display:block;font-size:7px;font-weight:700}
.news-item h4{font-size:9.5px;color:var(--ink);font-weight:700}
.news-item p{font-size:8.5px;line-height:11px}
.news-item a{color:var(--orange);font-size:8.5px;text-decoration:none}

/* reasons */
.reason-title{left:74px;top:908px;font-family:"Noto Serif",Georgia,serif;font-weight:400;font-size:21px}
.reason-rule{left:74px;top:940px;width:300px;height:1px;background:var(--line)}
.reason-list{left:74px;top:952px;width:300px}
.reason{display:flex;gap:10px;height:42px}
.thumb{background:linear-gradient(135deg,#b9c2cb,#6f7a86);flex:none}
.reason .thumb{width:52px;height:34px}
.reason h4{font-size:9.5px;color:var(--orange);font-weight:700}
.reason p{font-size:8.5px;line-height:11px}
.videos{left:400px;top:912px;width:321px}
.video{display:flex;gap:10px;height:56px;padding-top:4px}
.video .thumb{width:64px;height:44px}
.video h4{font-size:11px;color:var(--ink);font-weight:600}
.video p{font-size:8.5px;line-height:11px}
.video a{font-size:8.5px;color:var(--orange);text-decoration:none}

/* footer */
.site-footer{left:0;top:1124px;width:796px;height:76px;background:var(--dark)}
.footer-col{top:8px;color:#ccc;font-size:8px;line-height:11px}
.footer-col h5{color:#fff;font-size:10px;margin-bottom:4px}
.team{display:flex;gap:8px}
.member{text-align:center;font-size:7.5px}
.member i{display:block;width:24px;height:24px;border-radius:50%;background:linear-gradient(#8a8a8a,#555);margin-bottom:2px}
.footer-brand{right:74px;top:10px;display:flex;align-items:center;gap:7px;color:#fff;font-weight:700;font-size:16px}
.footer-brand i{width:22px;height:22px;border-radius:50%;background:var(--orange)}
.social{right:74px;top:40px;display:flex;gap:5px}
.social i{width:14px;height:14px;border-radius:50%;background:#555}
.footer-bar{left:0;top:1186px;width:796px;height:14px;background:#0f0f0f;color:#999;font-size:7.5px;text-align:center;line-height:14px}
</style>
</head>
<body>

<header class="site-header abs">
  <div class="brand abs"><span class="brand-dot"></span>LumaVoltix</div>
  <nav class="main-nav abs">
    <a class="active" href="#">HOME</a><a href="#">FEATURES</a><a href="#">SECURITY</a><a href="#">SUPPORT</a>
  </nav>
</header>

<section class="hero abs">
  <h1 class="hero-title abs">WHAT IS VOLTCOIN?</h1>
  <p class="hero-text abs">Voltcoin is a digital currency you can use for personal transactions or business at high speed and low cost</p>
  <div class="hero-actions abs"><span class="btn">BEGIN</span><span class="btn">HOW TO BUY</span><span class="btn">HOW TO SELL</span></div>
  <div class="hero-art abs" role="img" aria-label="Illustration of a businessman holding a coin in front of a city skyline"></div>
</section>

<article class="feature highlight abs" style="left:74px">
  <h3>Stable And Secure</h3>
  <svg class="feature-icon" viewBox="0 0 22 22"><rect x="3" y="3" width="16" height="16" rx="2" fill="none" stroke="#fff" stroke-width="2"/><path d="M7 11l3 3 5-6" fill="none" stroke="#fff" stroke-width="2"/></svg>
  <p>Your funds stay safe in cold storage with daily audits and two step login.</p>
  <div class="more">READ MORE<i></i></div>
</article>
<article class="feature abs" style="left:297px">
  <h3>Highly Liquid</h3>
  <svg class="feature-icon" viewBox="0 0 22 22"><path d="M3 19h16M5 17V11M10 17V7M15 17V4" stroke="#3a7bc8" stroke-width="3"/></svg>
  <p>Deep order books and many active traders let you fill large orders fast.</p>
  <div class="more">READ MORE<i></i></div>
</article>
<article class="feature abs" style="left:519px">
  <h3>Professional</h3>
  <svg class="feature-icon" viewBox="0 0 22 22"><circle cx="11" cy="11" r="8" fill="none" stroke="#3a7bc8" stroke-width="2"/><path d="M11 6v5l3 3" stroke="#3a7bc8" stroke-width="2" fill="none"/></svg>
  <p>Advanced charts, open API access and support from a dedicated team.</p>
  <div class="more">READ MORE<i></i></div>
</article>

<h2 class="section-title market-title abs">MARKET OVERVIEW</h2>
<div class="market-rule abs"></div>
<div class="market-stats abs"><span>Market Cap: 35,585,441,045.00</span><span>Total VTC: 12,626,525 VTC</span></div>
<div class="chart abs">
  <div class="chart-tabs"><span>1h</span><span class="on">1d</span><span>1w</span><span>1m</span><span>3m</span><span>1y</span><span>All</span></div>
  <svg class="abs" style="left:10px;top:34px" width="380" height="206" viewBox="0 0 380 206">
    <g stroke="#e2e2e2" stroke-width="1"><line x1="30" y1="20" x2="375" y2="20"/><line x1="30" y1="60" x2="375" y2="60"/><line x1="30" y1="100" x2="375" y2="100"/><line x1="30" y1="140" x2="375" y2="140"/><line x1="30" y1="180" x2="375" y2="180"/></g>
    <g fill="#aaa" font-size="7" font-family="Open Sans, sans-serif"><text x="4" y="23">900</text><text x="4" y="63">700</text><text x="4" y="103">500</text><text x="4" y="143">300</text><text x="4" y="183">100</text>
    <text x="240" y="198">20 Apr</text><text x="280" y="198">22 Apr</text><text x="320" y="198">24 Apr</text><text x="355" y="198">26 Apr</text></g>
    <path d="M30 90 L55 70 L80 85 L105 60 L130 78 L155 72 L180 95 L205 88 L230 110 L255 104 L280 118 L305 112 L330 122 L355 116 L375 120 L375 180 L30 180Z" fill="#f7dcb8"/>
    <path d="M30 90 L55 70 L80 85 L105 60 L130 78 L155 72 L180 95 L205 88 L230 110 L255 104 L280 118 L305 112 L330 122 L355 116 L375 120" fill="none" stroke="var(--orange)" stroke-width="1.5"/>
  </svg>
</div>

<div class="news-tabs abs"><span class="tab-news">NEWS</span><span class="tab-old">OLD</span></div>
<div class="news-list abs">
  <div class="news-item"><div class="date"><b>25</b><small>MAY</small></div><div><h4>Market update for the week</h4><p>Trading volume rose again as new users joined</p><a href="#">Read more</a></div></div>
  <div class="news-item"><div class="date"><b>25</b><small>MAY</small></div><div><h4>New wallet features released</h4><p>Faster transfers and better security options now live</p><a href="#">Read more</a></div></div>
  <div class="news-item"><div class="date"><b>25</b><small>MAY</small></div><div><h4>Fees lowered for all traders</h4><p>Maker and taker fees drop starting this month</p><a href="#">Read more</a></div></div>
  <div class="news-item"><div class="date"><b>25</b><small>MAY</small></div><div><h4>Mobile app now available</h4><p>Trade on the go with our new phone application</p><a href="#">Read more</a></div></div>
</div>

<h2 class="reason-title abs">Our Reason for Being</h2>
<div class="reason-rule abs"></div>
<div class="reason-list abs">
  <div class="reason"><div class="thumb" role="img" aria-label="Photo of a trader at work"></div><div><h4>Open access to markets</h4><p>Anyone can buy and sell digital assets with ease and at low cost.</p></div></div>
  <div class="reason"><div class="thumb" role="img" aria-label="Photo of a team meeting"></div><div><h4>Trust and transparency</h4><p>Clear fees, public reserves and honest reporting every month.</p></div></div>
  <div class="reason"><div class="thumb" role="img" aria-label="Photo of a person using a laptop"></div><div><h4>Speed you can count on</h4><p>Orders match in milliseconds on our modern trading engine.</p></div></div>
  <div class="reason"><div class="thumb" role="img" aria-label="Photo of a support agent"></div><div><h4>Help when you need it</h4><p>Our support team answers questions day and night all week.</p></div></div>
</div>
<div class="videos abs">
  <div class="video"><div class="thumb" role="img" aria-label="Video still of an office"></div><div><h4>Theme Custom Colors Demo Video</h4><p>See how to change colours across the whole trading dashboard.</p><a href="#">Read more</a></div></div>
  <div class="video"><div class="thumb" role="img" aria-label="Video still of a workspace"></div><div><h4>Theme Fonts Demo Video</h4><p>Learn how to pick and set fonts for every page of the site.</p><a href="#">Read more</a></div></div>
  <div class="video"><div class="thumb" role="img" aria-label="Video still of a desk"></div><div><h4>Getting Started Guide</h4><p>A short tour of account setup, deposits and your first trade.</p><a href="#">Read more</a></div></div>
  <div class="video"><div class="thumb" role="img" aria-label="Video still of a meeting room"></div><div><h4>Security Basics Video</h4><p>Protect your account with strong passwords and two step login.</p><a href="#">Read more</a></div></div>
</div>

<footer class="site-footer abs">
  <div class="footer-col abs" style="left:74px"><h5>Contact Us</h5>Tel: 000 123 4567<br>No 14, Harbour Lane Street<br>North Vale, 00000</div>
  <div class="footer-col abs" style="left:270px"><h5>Our Team</h5>
    <div class="team"><div class="member"><i></i>Jonas</div><div class="member"><i></i>Mira</div><div class="member"><i></i>Theo</div></div>
  </div>
  <div class="footer-col abs" style="left:410px;width:150px"><h5>Blog</h5>Latest notes from our team on markets, safety and new product features.</div>
  <div class="footer-brand abs"><i></i>LumaVoltix</div>
  <div class="social abs"><i></i><i></i><i></i><i></i></div>
</footer>
<div class="footer-bar abs">fenrow.example © 2014 All Right reserved | Terms &amp; conditions</div>

</body>
</html>
```